TK Workshop - flyer

We are a machine shop. While making sales calls in the field, we need a flyer to leave behind with prospect to attract interest.

Target Market(s)

Medical device, aerospace and aviation component manfacturers

Font styles to use
Serif

Colors

Designer to choose colors to be used in the design.

Requirements
Must have
• NA
Nice to have
• NA
Should not have
• NA

```html
<!DOCTYPE html>
<html lang="en">
<head>
<meta charset="utf-8">
<title>TK Workshop – Flyer</title>
<link rel="stylesheet" href="https://fonts.googleapis.com/css2?family=Oswald:wght@400;600&family=Roboto+Condensed:wght@400;700&display=swap">
<style>
  :root {
    --blue: #1572bd;
    --blue-dark: #0e5a98;
    --blue-light: #1a80cf;
    --red: #e31e24;
    --white: #ffffff;
    --ink: #231f20;
    --backdrop: #e4e4e4;
    --photo-a: #8a7f74;
    --photo-b: #4d4a47;
  }
  * { margin: 0; padding: 0; box-sizing: border-box; }
  html, body { width: 927px; height: 1200px; overflow: hidden; }
  body { background: var(--backdrop); font-family: "Roboto Condensed", Arial, sans-serif; }
  .canvas { position: relative; width: 927px; height: 1200px; }
  .flyer { position: absolute; left: 110px; top: 142px; width: 707px; height: 915px; background: var(--white); overflow: hidden; }
  .abs { position: absolute; }

  .hero-photo { left: 0; top: 0; width: 707px; height: 400px; background: linear-gradient(160deg, #c9c3bb 0%, var(--photo-a) 45%, var(--photo-b) 100%); }
  .shapes { left: 0; top: 0; width: 707px; height: 915px; }

  .web { left: 403px; top: 30px; color: var(--white); font-size: 11px; font-weight: 700; letter-spacing: 5.8px; }
  .brand { left: 404px; top: 49px; width: 250px; height: 72px; background: var(--white); display: flex; flex-direction: column; justify-content: center; padding-left: 8px; }
  .brand-row { display: flex; align-items: center; gap: 10px; }
  .brand-name { font-family: "Oswald", sans-serif; font-weight: 400; font-size: 28px; color: var(--blue-dark); line-height: 1; }
  .brand-dot { width: 30px; height: 30px; border-radius: 50%; background: var(--red); }
  .brand-tag { font-size: 8.5px; color: var(--blue); letter-spacing: 1.3px; margin-top: 4px; }

  .inset { left: 38px; top: 153px; width: 180px; height: 180px; border-radius: 50%; border: 3px solid var(--red); background: radial-gradient(circle, #ffffff 30%, #e9eef2 100%); }

  .headline { left: 37px; top: 384px; color: var(--white); font-family: "Oswald", sans-serif; font-weight: 600; font-size: 45px; line-height: 45px; letter-spacing: 0.3px; }
  .specialty { left: 37px; top: 610px; color: var(--white); font-size: 13.5px; font-weight: 700; line-height: 16px; }
  .rule-left { left: 37px; top: 660px; width: 316px; height: 1px; background: rgba(255,255,255,.8); }
  .markets { left: 37px; top: 666px; color: var(--white); font-size: 21.5px; font-weight: 700; line-height: 28px; }
  .badge { left: 73px; top: 738px; width: 64px; height: 64px; border-radius: 50%; background: var(--white); }
  .shop-photo { left: 205px; top: 731px; width: 162px; height: 93px; background: linear-gradient(180deg, #9ea4a8, #55595c); }
  .cert { left: 37px; top: 813px; color: var(--white); font-size: 10.3px; font-weight: 700; }

  .intro { left: 392px; top: 360px; width: 312px; color: var(--ink); font-size: 12px; font-weight: 700; line-height: 14px; }
  .list { list-style: none; color: var(--ink); font-weight: 700; font-size: 22px; }
  .list li { position: relative; padding-left: 15px; }
  .list li::before { content: ""; position: absolute; left: 0; top: 11px; width: 7px; height: 7px; border-radius: 50%; background: var(--red); }
  .services { left: 388px; top: 441px; line-height: 27.4px; }
  .rule-right { left: 387px; top: 617px; width: 320px; height: 2px; background: var(--blue); }
  .equipment { left: 388px; top: 630px; line-height: 27.5px; font-size: 22.5px; }

  .footer { left: 0; top: 826px; width: 707px; height: 89px; background: var(--red); }
  .address { left: 0; top: 835px; width: 707px; text-align: center; color: var(--white); font-size: 22px; font-weight: 700; }
  .call-tab { left: 30px; top: 871px; }
  .call-tab svg { display: block; }
  .contact { left: 192px; top: 861px; color: var(--white); font-size: 30px; font-weight: 700; }
  .contact .email { font-size: 27px; }
</style>
</head>
<body>
<div class="canvas">
  <div class="flyer">
    <div class="abs hero-photo" role="img" aria-label="Photo of machined metal parts and inspection equipment on a workshop bench"></div>

    <svg class="abs shapes" width="707" height="915" viewBox="0 0 707 915">
      <rect x="0" y="0" width="707" height="63" fill="#1572bd"/>
      <polygon points="0,0 50,0 110,30 50,45 0,45" fill="#ffffff"/>
      <rect x="0" y="48" width="26" height="15" fill="#1572bd"/>
      <polygon points="0,63 150,63 120,95 0,168" fill="#ffffff"/>
      <polygon points="105,108 145,23 163,23 123,108" fill="#ffffff"/>
      <polygon points="135,108 175,23 193,23 153,108" fill="#ffffff"/>
      <polygon points="165,108 205,23 223,23 183,108" fill="#ffffff"/>
      <polygon points="195,108 235,23 253,23 213,108" fill="#ffffff"/>
      <polygon points="225,108 265,23 283,23 243,108" fill="#ffffff"/>
      <polygon points="270,30 385,63 270,96" fill="#ffffff"/>
      <polygon points="625,300 707,238 707,390 625,390" fill="#1572bd"/>
      <rect x="683" y="318" width="24" height="18" fill="#ffffff"/>
      <polygon points="370,322 430,322 620,390 707,390 707,826 370,826" fill="#ffffff"/>
      <polygon points="430,322 460,322 478,342 448,342" fill="#1572bd"/>
      <polygon points="468,328 490,328 508,350 486,350" fill="#1572bd"/>
      <polygon points="500,336 522,336 540,358 518,358" fill="#1572bd"/>
      <polygon points="532,344 560,344 580,370 552,370" fill="#1572bd"/>
      <polygon points="0,380 370,380 370,826 0,826" fill="#1572bd"/>
      <polygon points="210,450 320,380 350,380 240,450" fill="#1a80cf"/>
      <polygon points="160,850 300,600 320,600 180,850" fill="#1a80cf" opacity=".5"/>
      <polygon points="230,720 320,600 345,600 255,720" fill="#1a80cf" opacity=".5"/>
    </svg>

    <div class="abs web">www.tkworkshopcnc.com</div>
    <div class="abs brand">
      <div class="brand-row"><span class="brand-name">TK Workshop</span><span class="brand-dot"></span></div>
      <div class="brand-tag">Precision parts, built to last</div>
    </div>

    <div class="abs inset" role="img" aria-label="Colourful bone screws and implant connectors"></div>

    <h1 class="abs headline">MEDICAL AND<br>AEROSPACE<br>MANUFACTURING<br>AND ASSEMBLY<br>FACILITY</h1>
    <p class="abs specialty">specializing in bone plates and complex shapes<br>requiring multi-axis machining and inspection equipment</p>
    <div class="abs rule-left"></div>
    <p class="abs markets">Medical, Implants, Aerospace,<br>Aviation &amp; Military applications</p>
    <div class="abs badge" aria-hidden="true"></div>
    <div class="abs shop-photo" role="img" aria-label="Photo of the machine shop floor with CNC machines"></div>
    <p class="abs cert">ISO 13485, 9100, 9001 certified</p>

    <p class="abs intro">Our Education,<br>Training, and 25 years of Medical<br>and Aerospace machining experience<br>helps us determine the best possible methods<br>of manufacture that will be most cost effective for your parts.</p>
    <ul class="abs list services">
      <li>5 AXIS CNC MILLING</li>
      <li>TURNING</li>
      <li>CNC SWISS-TYPE</li>
      <li>DEBURRING</li>
      <li>LASER MARKING</li>
      <li>OPTIVISION SCOPE 300</li>
    </ul>
    <div class="abs rule-right"></div>
    <ul class="abs list equipment">
      <li>Coordinate measuring<br>machines, comparators,<br>surface plated micrometers</li>
      <li>Dedicated temperature<br>controlled room</li>
      <li>Ultrasonic cleaning &amp; reverse<br>osmosis water</li>
    </ul>

    <div class="abs footer"></div>
    <p class="abs address">4120 Birch Lane, Unit B, Valley Springs, CA 90000</p>
    <div class="abs call-tab">
      <svg width="152" height="24" viewBox="0 0 152 24">
        <polygon points="0,0 140,0 152,12 140,24 0,24" fill="#1572bd"/>
        <text x="8" y="17" fill="#ffffff" font-family="Roboto Condensed, sans-serif" font-weight="700" font-size="15">Call &amp; Email us at:</text>
      </svg>
    </div>
    <p class="abs contact">(555) 014-2280/<span class="email">info@tkworkshopcnc.com</span></p>
  </div>
</div>
</body>
</html>
```